Flyer Design Project- Wine Meditation

I require a flyer to be created for a course. It is a meditation course. So I want the cover design to look quirky but calm.

I have attached a previous design. The wording on the back should be the same only any reference to Chocolate should be changed to Wine. This project is for wine meditation. Although I have attached the previous flyer for guidance of the lay out and words used, I DO NOT want to to be a direct copy, I want it to look completely different. SO be creative. Any copies or anything that looks close to a copy will not even be considered.

I want the flyer to be A5 side but also the ability to resize it onto smaller cards.

I have also attached the wording for the back of the flyer in the attached word document.

If you need further information about the design breif please contact me.

Target Market(s)

20 to 40

Requirements
Must have
• Must have space for a logo which is currently being designed by the pixel harbour. For the time being insert the tall maple glen wellness logo which is attached.

Picture something realted to wine on the front and course detail on the back same as the attached sample.
Should not have
• a direct copy of my samples I have attached.

```html
<!DOCTYPE html>
<html lang="en">
<head>
<meta charset="utf-8">
<title>Wine Meditation Course – Flyer</title>
<link rel="stylesheet" href="https://fonts.googleapis.com/css2?family=Alegreya+Sans:wght@400;500&family=Cinzel:wght@400&family=Uncial+Antiqua&display=swap">
<style>
  :root {
    --orange-deep: #f5a01f;
    --orange: #f9b233;
    --orange-light: #fcd068;
    --wine: #b3141f;
    --wine-bright: #c8102e;
    --ember: #e8401c;
    --band: #c9231b;
    --cream: #f7c66e;
  }
  html, body {
    margin: 0;
    padding: 0;
    overflow: hidden;
    background: #ffffff;
  }
  .flyer {
    position: relative;
    width: 852px;
    height: 1200px;
    overflow: hidden;
    background: radial-gradient(ellipse 70% 55% at 55% 35%, var(--orange-light) 0%, var(--orange) 55%, var(--orange-deep) 100%);
    font-family: "Alegreya Sans", sans-serif;
    color: var(--wine);
  }
  .backdrop-pattern {
    position: absolute;
    left: 60px;
    top: 150px;
    width: 740px;
    height: 640px;
    border-radius: 50%;
    background: radial-gradient(circle, rgba(252, 208, 104, 0.0) 0%, rgba(245, 160, 31, 0.35) 100%);
  }
  .title {
    position: absolute;
    left: 0;
    top: 4px;
    width: 720px;
    text-align: center;
    margin: 0;
    font-family: "Uncial Antiqua", serif;
    font-weight: 400;
    font-size: 160px;
    line-height: 1;
    color: var(--wine-bright);
    letter-spacing: 4px;
  }
  .subtitle {
    position: absolute;
    left: 124px;
    top: 170px;
    margin: 0;
    font-family: "Cinzel", serif;
    font-weight: 400;
    font-size: 40px;
    letter-spacing: 9px;
    color: var(--wine);
    white-space: nowrap;
  }
  .copy {
    position: absolute;
    left: 20px;
    width: 812px;
    text-align: center;
  }
  .heading {
    margin: 0;
    font-weight: 400;
    line-height: 1.1;
  }
  .heading--md { font-size: 31px; }
  .heading--sm { font-size: 23px; }
  .heading--lg { font-size: 32px; }
  .body-text {
    margin: 0;
    font-size: 18.5px;
    line-height: 24.5px;
  }
  .intro { top: 226px; }
  .hangover { top: 352px; }
  .benefits-title { top: 496px; }
  .benefits {
    position: absolute;
    top: 544px;
    left: 0;
    margin: 0;
    padding: 0;
    list-style: none;
    font-size: 19px;
    line-height: 24px;
  }
  .benefits li {
    position: absolute;
    white-space: nowrap;
  }
  .benefits li::before {
    content: "•";
    margin-right: 2px;
  }
  .benefits .wrap { white-space: normal; width: 460px; text-indent: -8px; padding-left: 8px; }
  .illustration {
    position: absolute;
    left: 0;
    top: 520px;
    width: 330px;
    height: 620px;
    border-radius: 0 60% 0 0 / 0 30% 0 0;
    background: linear-gradient(180deg, rgba(232, 64, 28, 0.55) 0%, var(--ember) 60%, var(--band) 100%);
  }
  .flourish {
    position: absolute;
    left: 330px;
    top: 780px;
    width: 522px;
    height: 320px;
    background: radial-gradient(ellipse 60% 60% at 70% 40%, rgba(232, 64, 28, 0.35) 0%, rgba(232, 64, 28, 0) 100%);
  }
  .base-band {
    position: absolute;
    left: 0;
    bottom: 0;
    width: 852px;
    height: 110px;
  }
  .client-name {
    position: absolute;
    left: 630px;
    top: 968px;
    width: 200px;
    margin: 0;
    font-family: "Alegreya Sans", sans-serif;
    font-weight: 500;
    font-size: 38px;
    line-height: 38px;
    color: var(--wine);
    text-align: left;
  }
  .contact {
    position: absolute;
    left: 460px;
    top: 1138px;
    margin: 0;
    font-family: "Cinzel", serif;
    font-size: 21px;
    line-height: 26px;
    color: var(--cream);
    letter-spacing: 0.5px;
  }
</style>
</head>
<body>
<main class="flyer">
  <div class="backdrop-pattern" role="img" aria-label="Faint circular labyrinth pattern in soft orange"></div>

  <h1 class="title">WINE</h1>
  <p class="subtitle">MEDITATION COURSE</p>

  <section class="copy intro">
    <h2 class="heading heading--md">Wine What?!</h2>
    <p class="body-text">Yes, you read right. WINE MEDITATION! What could be better than combining<br>
    the delectable taste of wine with meditation, right? Well that is exactly what<br>
    this course is all about with a little bit of mindfulness thrown in.</p>
  </section>

  <section class="copy hangover">
    <h2 class="heading heading--sm">Learn to drink wine without the hangover!</h2>
    <h2 class="heading heading--md">NO HANGOVER! Really?</h2>
    <p class="body-text" style="margin-top:6px">It’s true because we challenge you to the fact that you have never really savored<br>
    your glass of wine. So we are going to teach you how to do it MINDFULLY.<br>
    This way you are guaranteed not to get a hangover while drinking wine.</p>
  </section>

  <section class="copy benefits-title">
    <h2 class="heading heading--lg">What you get with the course:</h2>
  </section>

  <div class="illustration" role="img" aria-label="Illustration of a seated woman with a ponytail holding a glass of red wine"></div>
  <div class="flourish" role="img" aria-label="Decorative red flower and starburst ornaments"></div>

  <ul class="benefits">
    <li style="left:268px;top:0">A wine meditation course book.</li>
    <li style="left:298px;top:34px">Mindfulness and meditation instruction online.</li>
    <li style="left:320px;top:68px">Learn how to drink wine mindfully.</li>
    <li style="left:343px;top:103px">Learn meditation techniques and postures.</li>
    <li style="left:352px;top:137px">FREE mp3 guided meditation download.</li>
    <li class="wrap" style="left:352px;top:171px">5% of the course goes to charity – Please see our website for this month’s charitable cause.</li>
  </ul>

  <p class="client-name">TALL MAPLE GLEN Wellness</p>

  <svg class="base-band" viewBox="0 0 852 110" aria-hidden="true">
    <path d="M0 14 C 120 2, 220 22, 340 12 S 600 0, 720 10 S 820 8, 852 4 L 852 110 L 0 110 Z" fill="var(--band)"/>
  </svg>

  <p class="contact">WWW.VINE-STILLNESS.COM<br>PHONE (02) 5550 0147</p>
</main>
</body>
</html>
```